Tradeshow Banner Design (Qty2, 6'H x 2'W)

Brightwell Contractors is an Electrical, Fire Alarm, and Security Contracting company. For tradeshows, we would like 2 vertical Banners to put behind our booth. Our colors are Red, Grey & Black. I would like the Banners to be informative on what services we provide, with some appealing Graphic Design. (bwc-kmo.com)
Slogan: Safeguarding Communities Electrical, Fire & Security Solutions
Target Market(s)
Commercial Construction Clients
Industry/Entity Type
Electrical / Construction
Font styles to use
Other font styles liked:
- Aileron
Colors
EB3D1F
EC4F4E
F09395
F8D3D4
FCEDEE
Requirements
Must have
- Our Logo, Color Scheme, Brief Caption of the services we provide
Nice to have
- Appealing Imagery & a modern/simplistic design

```html
<!DOCTYPE html>
<html lang="en">
<head>
<meta charset="utf-8">
<title>Brightwell Contractors – Tradeshow Banner</title>
<link rel="stylesheet" href="https://fonts.googleapis.com/css2?family=Archivo:wght@400;500;700;800&family=Figtree:wght@400;500&display=swap">
<style>
:root{
  --red:#EB3D1F;
  --brand-red:#ED2426;
  --coral:#EC4F4E;
  --rose:#F09395;
  --blush:#F8D3D4;
  --paper:#FCEDEE;
  --grey:#5a5a5c;
  --ink:#3b3b3d;
  --white:#ffffff;
  --hat:#f2c230;
  --skin:#d9a48a;
  --belt:#3e3f44;
  --housing:#e4e6e2;
  --post:#f0d04a;
}
*{margin:0;padding:0;box-sizing:border-box}
html,body{width:1200px;height:3599px;overflow:hidden;background:var(--paper)}
.banner{position:relative;width:1200px;height:3599px;overflow:hidden;background:var(--paper);font-family:"Figtree",sans-serif;color:var(--ink)}
.abs{position:absolute}

/* brand */
.brand-mark{left:300px;top:123px;width:252px;height:252px;border-radius:50%;background:var(--brand-red)}
.brand-name{left:566px;top:146px;font-family:"Archivo",sans-serif;font-weight:500;color:var(--grey);font-size:66px;line-height:80px;letter-spacing:-1.5px}
.brand-tag{left:568px;top:322px;font-family:"Archivo",sans-serif;font-weight:500;color:var(--grey);font-size:28px;letter-spacing:-.5px}

/* section rails */
.rail{width:3px;background:var(--red)}
.rail-dot{width:22px;height:22px;border-radius:50%;border:3px solid var(--red);background:var(--paper)}

/* headings */
.section-title{font-family:"Archivo",sans-serif;font-weight:800;color:var(--red);font-size:140px;line-height:122px;letter-spacing:-3px}
.section-title.right{text-align:right}

.service h3{font-family:"Archivo",sans-serif;font-weight:500;color:var(--ink);font-size:42px;line-height:35px;letter-spacing:-.5px;margin-bottom:30px}
.service ul{list-style:none}
.service li{font-size:20.5px;line-height:23px;color:var(--ink);margin-bottom:13px}
.service li::before{content:"- ";color:var(--grey)}

.photo{border-radius:50%}
.photo-electrical{
  background:
    radial-gradient(ellipse 34% 30% at 88% 16%,var(--hat) 0%,rgba(242,194,48,.6) 45%,rgba(242,194,48,0) 100%),
    radial-gradient(ellipse 45% 28% at 40% 22%,var(--skin) 0%,rgba(217,164,138,.5) 50%,rgba(217,164,138,0) 100%),
    radial-gradient(ellipse 48% 42% at 74% 72%,var(--belt) 0%,rgba(62,63,68,.75) 45%,rgba(62,63,68,0) 100%),
    radial-gradient(circle at 60% 45%,var(--coral),#e24846 70%);
}
.photo-security{
  background:
    radial-gradient(ellipse 48% 22% at 68% 28%,var(--housing) 0%,rgba(228,230,226,.75) 50%,rgba(228,230,226,0) 100%),
    radial-gradient(ellipse 30% 22% at 32% 52%,#d8dad6 0%,rgba(216,218,214,.6) 50%,rgba(216,218,214,0) 100%),
    radial-gradient(ellipse 30% 32% at 22% 84%,var(--post) 0%,rgba(240,208,74,.7) 50%,rgba(240,208,74,0) 100%),
    radial-gradient(circle at 45% 45%,var(--coral),#e24846 70%);
}

/* footer */
.footer{left:0;top:3192px;width:1200px;height:407px;background:var(--coral);color:var(--white)}
.footer-cta{position:absolute;left:0;top:64px;width:1200px;text-align:center;font-family:"Archivo",sans-serif;font-weight:700;font-size:39px;letter-spacing:-1.2px}
.areas{position:absolute;left:92px;top:140px;font-family:"Archivo",sans-serif;font-size:31px;line-height:35px;text-transform:uppercase}
.areas b{font-weight:700}
.contact{position:absolute;right:89px;top:134px;text-align:right;font-family:"Archivo",sans-serif;font-weight:700}
.contact .line{display:flex;justify-content:flex-end;align-items:center;gap:10px;font-size:32px;line-height:44px}
.contact .addr{font-size:23px;line-height:25px;margin-top:4px}
.contact svg{flex:none}
.social{position:absolute;top:323px;font-family:"Figtree",sans-serif;font-size:30px;display:flex;align-items:center;gap:12px}
.social .sq{width:30px;height:30px;border:3px solid var(--white);border-radius:6px}
</style>
</head>
<body>
<main class="banner">

  <header>
    <div class="abs brand-mark"></div>
    <div class="abs brand-name">BRIGHTWELL<br>CONTRACTORS</div>
    <div class="abs brand-tag">ELECTRICAL | FIRE | SECURITY</div>
  </header>

  <section>
    <div class="abs photo photo-electrical" role="img" aria-label="Electrician in yellow hard hat and tool belt writing on a clipboard" style="left:416px;top:657px;width:964px;height:964px"></div>
    <div class="abs rail" style="left:77px;top:552px;height:892px"></div>
    <div class="abs rail-dot" style="left:68px;top:1065px"></div>
    <div class="abs rail-dot" style="left:68px;top:1432px"></div>
    <h1 class="abs section-title" style="left:110px;top:555px">ELECT-<br>RICAL</h1>
    <div class="abs service" style="left:122px;top:1062px">
      <h3>Electrical<br>Installation<br>&amp; Repair</h3>
      <ul>
        <li>Full electrical services</li>
        <li>Licensed Electricians</li>
        <li>LED retrofitting expertise</li>
        <li>Versatile one-stop-shop for<br>customer satisfaction</li>
        <li>24/7 emergency repairs</li>
      </ul>
    </div>
    <div class="abs service" style="left:122px;top:1430px">
      <h3>Structured<br>Wiring</h3>
      <ul>
        <li>Speeds up businesses with wiring solutions</li>
        <li>Expert installation for seamless security, networking</li>
        <li>Professional, wire-free look</li>
        <li>Boosts tech adoption confidence</li>
      </ul>
    </div>
  </section>

  <section>
    <div class="abs photo photo-security" role="img" aria-label="White CCTV security camera mounted on a yellow post" style="left:-266px;top:1849px;width:964px;height:964px"></div>
    <div class="abs rail" style="left:1120px;top:1795px;height:964px"></div>
    <div class="abs rail-dot" style="left:1111px;top:2416px"></div>
    <div class="abs rail-dot" style="left:1111px;top:2748px"></div>
    <h1 class="abs section-title right" style="right:124px;top:1800px">SECU-<br>RITY</h1>
    <div class="abs service" style="left:748px;top:2408px">
      <h3>Security<br>Monitoring</h3>
      <ul>
        <li>Fast emergency alarm response</li>
        <li>Varied security/fire systems</li>
        <li>Wireless connectivity persists<br>during power cuts</li>
        <li>Motion detectors and sensors</li>
        <li>Manual trigger option</li>
      </ul>
    </div>
    <div class="abs service" style="left:748px;top:2742px">
      <h3>Surveillance</h3>
      <ul>
        <li>Monitoring via CCTV/IP cameras</li>
        <li>Ensures premises and staff safety</li>
        <li>Cellular-connected cameras allow<br>recording during outages</li>
        <li>Accessible via smartphones</li>
        <li>Enhances business control</li>
      </ul>
    </div>
  </section>

  <footer class="abs footer">
    <div class="footer-cta">LET US HELP YOU PROTECT YOUR BUSINESS TODAY</div>
    <div class="areas">Serving <b>Auburn, Kent,<br>Renton, Seattle, Bellevue,<br>Lynnwood, Maple Valley,<br>Covington, Puyallup</b></div>
    <div class="contact">
      <div class="line">
        <svg width="32" height="32" viewBox="0 0 32 32"><circle cx="16" cy="16" r="16" fill="#fff"/><path d="M11 8c1 0 2 3 2.5 4.5.3 1-1.5 2-1.2 2.8.8 2 2.5 3.7 4.4 4.5.8.3 1.8-1.5 2.8-1.2 1.5.5 4.5 1.5 4.5 2.5 0 1.5-1.8 3-3.5 3C14.5 24 8 17.5 8 11.5 8 9.8 9.5 8 11 8z" fill="#EC4F4E"/></svg>
        <span>555-014-2290</span>
      </div>
      <div class="line">
        <svg width="32" height="32" viewBox="0 0 32 32"><circle cx="16" cy="16" r="14.5" fill="none" stroke="#fff" stroke-width="3"/><rect x="9" y="11" width="14" height="10" fill="none" stroke="#fff" stroke-width="2"/><path d="M9 11l7 6 7-6" fill="none" stroke="#fff" stroke-width="2"/></svg>
        <span>office@bwc-kmo.com</span>
      </div>
      <div class="line addr">
        <svg width="30" height="34" viewBox="0 0 30 34"><path d="M15 2C8 2 3 7 3 13.5 3 22 15 32 15 32s12-10 12-18.5C27 7 22 2 15 2z" fill="none" stroke="#fff" stroke-width="3"/><circle cx="15" cy="13.5" r="4.5" fill="#fff"/></svg>
        <span>2250 Harbor Crest Rd STE 210<br>Auburn, WA 98001</span>
      </div>
    </div>
    <div class="social" style="left:92px"><span class="sq"></span><span>bwc_kmo</span></div>
    <div class="social" style="right:89px"><span class="sq"></span><span>BrightwellContractors</span></div>
  </footer>

</main>
</body>
</html>
```